Business Cards for new orthopaedic surgery practice

My husband and I are starting our own orthopaedic surgery practice. We are looking for a business card that is uniform, but one will have my name/title and the other will have his. You can just create one design with my name on it for now. But when I choose your design as the winning design I will ask that you add another copy with his name/title.

We are looking for classy, simple, elite all in one. We like dark blues/a little gold/yellow. Something that goes with our logo. We want our logo incorporated. Here is all the info you need:
Business name: RV Spine & Vitality Center
Location: 38915 North Bramble Ave
Maple Harbor, FL 33990
Phone: 954-218-4630
Fax: 954-571-2846
Email: info@myrvspine.example

Names: Lucinda Ferrow, M.D.
Board Certified Hand and Upper Extremity Surgeon

Emeka Dlunga, M.D.
Board Certified Hip & Knee Replacement/General Orthopaedic Surgeon

Can decide what you want to put on the back. Maybe a slogan:
Rooted in Care. Focused on You

I am just going to upload our logo. The only thing is if we select you as the winning design, the location, and phone numbers may change. We will need your help to update that once fully solidified.

Industry/Entity Type

Medical

Contact Information for Business Card

Colors
0054AA
0677BA
7BADD7
CADEEF
E8F1F8
0094D4
00A9DD
6FCCEA
C7EBF8
E9F6FB

Requirements
Must have
• class, appeal,
Should not have
• We want to air on the side of masculine if we are looking at masculine vs. feminine feel. But we still want it classy, sophisticated, and something we will love

```html
<!DOCTYPE html>
<html lang="en">
<head>
<meta charset="utf-8">
<title>RV Spine &amp; Vitality Center – Business Cards</title>
<link href="https://fonts.googleapis.com/css2?family=Oswald:wght@300;400;500&display=swap" rel="stylesheet">
<style>
  :root {
    --brand-blue: #0a33bd;
    --card-white: #ffffff;
    --sky-top-left: #2ef8fb;
    --sky-top-right: #00d2f5;
    --sea-left: #5ee6d8;
    --sea-right: #009c80;
    --text-light: #ffffff;
  }
  * { margin: 0; padding: 0; box-sizing: border-box; }
  html, body { width: 1200px; height: 1200px; overflow: hidden; }
  body { font-family: "Oswald", "Arial Narrow", sans-serif; }

  .canvas { position: relative; width: 1200px; height: 1200px; overflow: hidden; }
  .backdrop-top {
    position: absolute; left: 0; top: 0; width: 1200px; height: 666px;
    background: linear-gradient(90deg, var(--sky-top-left), var(--sky-top-right));
  }
  .backdrop-bottom {
    position: absolute; left: 0; top: 666px; width: 1200px; height: 534px;
    background: linear-gradient(160deg, var(--sea-left) 0%, #1cd3c0 45%, var(--sea-right) 100%);
  }

  .card { position: absolute; box-shadow: 2px 3px 5px rgba(0,0,0,0.35); overflow: hidden; }
  .card--front { background: var(--card-white); }
  .card--back { background: var(--brand-blue); color: var(--text-light); }

  .logo-panel { position: absolute; left: 151px; top: 0; width: 281px; height: 515px; background: var(--card-white); }

  .brand-mark {
    position: absolute; transform: translate(-50%, -50%);
    display: flex; flex-direction: column; align-items: center; gap: 5px;
    color: var(--brand-blue); font-weight: 400; text-transform: uppercase;
    text-align: center; line-height: 1.1; letter-spacing: 0.04em; white-space: nowrap;
  }
  .brand-mark__dot { width: 16px; height: 16px; border-radius: 50%; background: var(--brand-blue); }
  .brand-mark--large { font-size: 20px; }
  .brand-mark--large .brand-mark__dot { width: 22px; height: 22px; }
  .brand-mark--small { font-size: 14px; }

  .web-address {
    position: absolute; font-size: 10px; font-weight: 500; color: var(--brand-blue);
    letter-spacing: 0.06em; white-space: nowrap; line-height: 12px;
  }
  .accent-bar { position: absolute; background: var(--brand-blue); }

  .doctor-name { position: absolute; font-size: 22px; font-weight: 400; letter-spacing: 0.1em; line-height: 26px; white-space: nowrap; }
  .doctor-title { position: absolute; font-size: 9.5px; font-weight: 400; letter-spacing: 0.06em; line-height: 17px; white-space: nowrap; }
  .contact-list { position: absolute; list-style: none; font-size: 9.5px; letter-spacing: 0.06em; }
  .contact-list li { height: 21.6px; line-height: 21.6px; white-space: nowrap; }
  .divider { position: absolute; width: 1px; background: var(--text-light); }

  .card--v-front { left: 600px; top: 52px; width: 238px; height: 426px; }
  .card--v-back { left: 880px; top: 52px; width: 240px; height: 426px; }
  .card--h-front-a { left: 83px; top: 583px; width: 427px; height: 238px; }
  .card--h-front-b { left: 692px; top: 583px; width: 427px; height: 238px; }
  .card--h-back-a { left: 83px; top: 863px; width: 427px; height: 238px; }
  .card--h-back-b { left: 692px; top: 863px; width: 427px; height: 238px; }
</style>
</head>
<body>
<div class="canvas">
  <div class="backdrop-top"></div>
  <div class="backdrop-bottom"></div>

  <div class="logo-panel">
    <div class="brand-mark brand-mark--large" style="left:145px; top:334px;">
      <span class="brand-mark__dot"></span>
      <span>RV Spine &amp; Vitality<br>Center</span>
    </div>
  </div>

  <div class="card card--front card--v-front">
    <div class="brand-mark brand-mark--small" style="left:118px; top:196px;">
      <span class="brand-mark__dot"></span>
      <span>RV Spine &amp; Vitality<br>Center</span>
    </div>
    <div class="accent-bar" style="left:0; top:401px; width:80px; height:25px;"></div>
    <div class="web-address" style="left:94px; top:407px;">www.rvspinevitality.example</div>
  </div>

  <div class="card card--back card--v-back">
    <div class="doctor-name" style="left:17px; top:145px;">Lucinda Ferrow, M.D.</div>
    <div class="doctor-title" style="left:17px; top:170px;">Board Certified Hand and Upper<br>Extremity Surgeon</div>
    <ul class="contact-list" style="left:17px; top:277px;">
      <li>Location: 38915 North Bramble Ave</li>
      <li>Maple Harbor, FL 33990</li>
      <li>Phone: 954-218-4630</li>
      <li>Fax: 954-571-2846</li>
      <li>Email: info@myrvspine.example</li>
    </ul>
  </div>

  <div class="card card--front card--h-front-a">
    <div class="brand-mark brand-mark--small" style="left:222px; top:122px;">
      <span class="brand-mark__dot"></span>
      <span>RV Spine &amp; Vitality<br>Center</span>
    </div>
    <div class="web-address" style="left:31px; top:214px;">www.rvspinevitality.example</div>
    <div class="accent-bar" style="left:189px; top:212px; width:238px; height:26px;"></div>
  </div>

  <div class="card card--front card--h-front-b">
    <div class="brand-mark brand-mark--small" style="left:222px; top:122px;">
      <span class="brand-mark__dot"></span>
      <span>RV Spine &amp; Vitality<br>Center</span>
    </div>
    <div class="web-address" style="left:31px; top:214px;">www.rvspinevitality.example</div>
    <div class="accent-bar" style="left:189px; top:212px; width:238px; height:26px;"></div>
  </div>

  <div class="card card--back card--h-back-a">
    <div class="doctor-name" style="left:28px; top:25px;">Lucinda Ferrow, M.D.</div>
    <div class="doctor-title" style="left:28px; top:50px;">Board Certified Hand and Upper<br>Extremity Surgeon</div>
    <div class="divider" style="left:222px; top:119px; height:105px;"></div>
    <ul class="contact-list" style="left:242px; top:112px;">
      <li>Location: 38915 North Bramble Ave</li>
      <li>Maple Harbor, FL 33990</li>
      <li>Phone: 954-218-4630</li>
      <li>Fax: 954-571-2846</li>
      <li>Email: info@myrvspine.example</li>
    </ul>
  </div>

  <div class="card card--back card--h-back-b">
    <div class="doctor-name" style="left:28px; top:25px;">Emeka Dlunga, M.D.</div>
    <div class="doctor-title" style="left:28px; top:50px;">Board Certified Hip &amp; Knee Replacement/<br>General Orthopaedic Surgeon</div>
    <div class="divider" style="left:222px; top:119px; height:105px;"></div>
    <ul class="contact-list" style="left:242px; top:112px;">
      <li>Location: 38915 North Bramble Ave</li>
      <li>Maple Harbor, FL 33990</li>
      <li>Phone: 954-218-4630</li>
      <li>Fax: 954-571-2846</li>
      <li>Email: info@myrvspine.example</li>
    </ul>
  </div>
</div>
</body>
</html>
```